KVRo Business Cards

We need a business card design. We are a Technology (Audio Visual) design, sales and installation company. Looking for a double sided design, clean

Contact Information for Business Card

Clean, modern look, 2 sided

Font styles to use
Sans Serif

```html
<!DOCTYPE html>
<html lang="en">
<head>
<meta charset="utf-8">
<title>KVRo Business Cards</title>
<link rel="stylesheet" href="https://fonts.googleapis.com/css2?family=Arimo:wght@400;700&display=swap">
<style>
  :root {
    --stage: #1c1c1d;
    --stage-light: #2a2a2b;
    --card-front: #232324;
    --card-back: #141414;
    --accent: #f4a01c;
    --text-light: #d9d9d9;
    --text-muted: #a9a9a9;
    --gloss-dark: #1d1d1e;
  }
  * { box-sizing: border-box; margin: 0; padding: 0; }
  html, body {
    width: 1200px; height: 800px; overflow: hidden;
    background: radial-gradient(ellipse at 50% 30%, var(--stage-light), var(--stage) 70%);
    font-family: "Arimo", Arial, sans-serif;
  }
  .stage {
    position: relative; width: 1200px; height: 800px;
    display: flex; align-items: center; justify-content: center; gap: 40px;
  }
  .card {
    position: relative; width: 540px; height: 308px;
    box-shadow: 0 18px 40px rgba(0,0,0,.55);
  }
  .card--back { background: var(--card-back); display: flex; align-items: center; justify-content: center; }
  .card--back .tone-pattern {
    position: absolute; inset: 0;
    background: linear-gradient(135deg, var(--gloss-dark), #0d0d0d 60%, var(--gloss-dark));
  }
  .card--back .wordmark {
    position: relative; color: var(--text-light); font-weight: 400; font-size: 26px; letter-spacing: 6px;
  }
  .card--front { background: var(--card-front); }
  .brand {
    position: absolute; right: 34px; top: 30px; text-align: right;
  }
  .brand .wordmark {
    display: block; color: var(--text-light); font-weight: 400; font-size: 28px; line-height: 1; letter-spacing: 6px;
  }
  .brand .web {
    display: block; color: var(--text-muted); font-size: 10px; margin-top: 6px; letter-spacing: 1px;
  }
  .rule { position: absolute; height: 1.5px; background: var(--accent); }
  .rule--top { left: 236px; right: 30px; top: 90px; }
  .rule--mid { left: 40px; width: 270px; top: 170px; }
  .person { position: absolute; left: 40px; top: 108px; }
  .person .name { color: var(--accent); font-size: 22px; }
  .person .role { color: var(--text-light); font-size: 13px; margin-top: 3px; }
  .contact { position: absolute; display: flex; gap: 9px; align-items: flex-start; }
  .contact svg { flex: none; margin-top: 7px; }
  .contact .label { color: var(--accent); font-size: 14px; }
  .contact .value { color: var(--text-light); font-size: 11px; line-height: 1.3; }
  .contact--address { left: 40px; top: 206px; }
  .contact--phone { left: 40px; top: 258px; }
  .contact--email { left: 340px; top: 206px; }
</style>
</head>
<body>
<main class="stage">
  <section class="card card--back" aria-label="Card back">
    <div class="tone-pattern" role="img" aria-label="Tonal spot-gloss repeated name pattern across the card"></div>
    <span class="wordmark">KVRo</span>
  </section>

  <section class="card card--front" aria-label="Card front">
    <div class="brand">
      <span class="wordmark">KVRo</span>
      <span class="web">kvro-av.com</span>
    </div>
    <div class="rule rule--top"></div>
    <div class="person">
      <p class="name">Rohan Malhotra</p>
      <p class="role">Managing Director</p>
    </div>
    <div class="rule rule--mid"></div>

    <div class="contact contact--address">
      <svg width="22" height="22" viewBox="0 0 22 22" aria-hidden="true">
        <path d="M5 0h17v17a5 5 0 0 1-5 5H0V5a5 5 0 0 1 5-5z" fill="var(--accent)"/>
        <path d="M11 5a3.5 3.5 0 0 0-3.5 3.5c0 2.6 3.5 7 3.5 7s3.5-4.4 3.5-7A3.5 3.5 0 0 0 11 5zm0 5a1.4 1.4 0 1 1 0-2.8 1.4 1.4 0 0 1 0 2.8z" fill="var(--card-front)"/>
      </svg>
      <div>
        <p class="label">Address</p>
        <p class="value">Lakeview Road 2nd Block 4th Cross,<br>Indira nagar, Bangalore-560038</p>
      </div>
    </div>

    <div class="contact contact--phone">
      <svg width="22" height="22" viewBox="0 0 22 22" aria-hidden="true">
        <path d="M5 0h17v17a5 5 0 0 1-5 5H0V5a5 5 0 0 1 5-5z" fill="var(--accent)"/>
        <path d="M8 6l2 2.2-1 1.4c.7 1.4 1.6 2.3 3 3l1.4-1 2.2 2-1.3 1.7c-3.5-.4-7.2-4.1-7.6-7.6z" fill="var(--card-front)"/>
      </svg>
      <div>
        <p class="label">Phone</p>
        <p class="value">+ 91 987 654 3210</p>
      </div>
    </div>

    <div class="contact contact--email">
      <svg width="22" height="22" viewBox="0 0 22 22" aria-hidden="true">
        <path d="M5 0h17v17a5 5 0 0 1-5 5H0V5a5 5 0 0 1 5-5z" fill="var(--accent)"/>
        <rect x="6" y="7" width="10" height="8" fill="var(--card-front)"/>
        <path d="M6 7l5 4 5-4" fill="none" stroke="var(--accent)" stroke-width="1"/>
      </svg>
      <div>
        <p class="label">Email</p>
        <p class="value">hello@kvro-av.com</p>
      </div>
    </div>
  </section>
</main>
</body>
</html>
```